Freelance film producer/editor wants you to brisk vanta!

'Brisk Vanta' is my production business based in Melbourne, though I do a fair bit of work overseas. I'm a one woman show most of the time but enlist other crew members for larger projects. I manage productions from start to finish including producing, filming, editing, distribution, photography and animation.

My current tag line and details are as follows:

Greta Hollensby
Producer. Editor. Thinker.
[M] +61 417 562 093
[E] gh[at]briskvanta.com.au
www.briskvanta.com.au

I have a fairly wicked sense of humour and love a good pun, so feel free to work this into your design!

The final designs should demonstrate the areas I work in but not limited to. I'd rather not use old and typical "film" looking elements such as a clapper or negative reel. Having said that, the logo itself (attached) is quite typical because the first 'o' is a closed aperture and the second is a wide aperture. Happy for the logo to be pulled apart for the business card to be more interesting.

The majority of projects I work on are quite different and in some cases a bit crazy. Lots of travel involved. The main difference between me and other producers is that I don't say I work in 'film', even though i do. I want the card to leave me open to new roles and projects as opposed to squashing myself into one particular category.

I'm open to colour but prefer a simple design that isn't too hectic.

I have also attached an example I did like that was printed on plastic but then I realised so many other people had ripped it off....

I'm open to paper board or plastic (transparent) designs etc. One sided or two sided.

Thanks for sharing your ideas with me and please, go as nuts as you want to with this! :)

Target Market(s)

My clients range from non profits in health and educational institutions to record labels and well known artists. The business attracts corporates as well though the majority of my business is achieved through referral and word of mouth so most people will soon realise that my personality and work are very much intertwined and the reason they hire me for a job.

Industry/Entity Type

Business

Font styles to use
Other font styles liked:
• Eurostile or similar

Requirements
Must have
• I have a very open mind when it comes to design. I do like the existing tag line but if you can come up with something better I'm all ears! (and eyes)

Nice to have
• Back of the business card can be graphics, there can be transparent elements or holes, embossing options...
Should not have
• Besides my name, nothing should scream "I am woman!" because in my industry that's not a selling point.

The colour pink is a definite no.

```html
<!DOCTYPE html>
<html lang="en">
<head>
<meta charset="utf-8">
<title>Brisk Vanta – Business Card</title>
<link rel="stylesheet" href="https://fonts.googleapis.com/css2?family=Saira:wght@300;400&display=swap">
<style>
  :root {
    --page: #f1f1f1;
    --card: #ffffff;
    --ink: #111111;
    --rule: #4a4a4a;
    --band: #000000;
    --band-text: #ffffff;
    --pattern-dark: #141414;
    --pattern-light: #8a8a8a;
  }
  * { box-sizing: border-box; margin: 0; padding: 0; }
  html, body {
    width: 1200px; height: 544px; overflow: hidden;
    background: var(--page);
    font-family: "Saira", "Helvetica Neue", Arial, sans-serif;
    color: var(--ink);
  }
  .stage { position: relative; width: 1200px; height: 544px; }

  .card {
    position: absolute; top: 38px;
    width: 573px; height: 354px;
    background: var(--card);
    overflow: hidden;
    box-shadow: 0 1px 3px rgba(0,0,0,0.15);
  }
  .card--front { left: 16px; }
  .card--back  { left: 610px; }

  /* front */
  .front-art { position: absolute; inset: 0; }
  .front-art .rule { stroke: var(--rule); stroke-width: 3; }
  .front-art .ball { fill: var(--ink); }

  .wordmark {
    position: absolute; top: 28px; left: 0; right: 0;
    text-align: center;
    font-weight: 300; font-size: 56px; letter-spacing: 1px;
    line-height: 1;
  }
  .identity {
    position: absolute; top: 164px; left: 10px; right: 0;
    text-align: center; line-height: 1.4;
  }
  .identity .name { font-size: 22px; font-weight: 400; }
  .identity .tagline { font-size: 19px; font-weight: 400; }

  .web-band {
    position: absolute; left: 0; right: 0; bottom: 0; height: 42px;
    background: var(--band); color: var(--band-text);
    display: flex; align-items: center; justify-content: center;
    font-size: 19px; letter-spacing: 0.3px; padding-left: 10px;
  }

  /* back */
  .pattern-field {
    position: absolute; inset: 0;
    background: repeating-linear-gradient(135deg, var(--pattern-dark) 0 14px, var(--pattern-light) 14px 28px);
  }
  .badge {
    position: absolute; left: 44px; top: 100px;
    width: 236px; height: 238px;
    background: var(--card);
    border: 2px solid var(--ink);
    border-radius: 18px;
    transform: rotate(9deg);
    display: flex; flex-direction: column; justify-content: center;
    padding-left: 22px;
  }
  .badge .word {
    font-weight: 300; font-size: 76px; line-height: 0.98;
    color: var(--ink);
  }
</style>
</head>
<body>
<main class="stage">

  <section class="card card--front" aria-label="Card front">
    <svg class="front-art" width="573" height="354" viewBox="0 0 573 354" aria-hidden="true">
      <line class="rule" x1="0" y1="87" x2="573" y2="121"/>
      <circle class="ball" cx="72" cy="74" r="15"/>
      <line class="rule" x1="0" y1="232" x2="484" y2="312"/>
      <circle class="ball" cx="404" cy="282" r="16"/>
    </svg>
    <h1 class="wordmark">brisk vanta</h1>
    <div class="identity">
      <p class="name">Greta Hollensby</p>
      <p class="tagline">Producer. Editor. Thinker.</p>
    </div>
    <footer class="web-band">www.briskvanta.com.au</footer>
  </section>

  <section class="card card--back" aria-label="Card back">
    <div class="pattern-field" role="img" aria-label="Black and white repeating pattern of camera aperture shapes"></div>
    <div class="badge">
      <span class="word">brisk</span>
      <span class="word">vanta</span>
    </div>
  </section>

</main>
</body>
</html>
```